Visual Print Advert for Hair & Makeup Artist

One page colour visual advertisement required for a hair and makeup artist business using pictures and logo with brief description and contact details. MUST have plain white background. All information will be provided I just need someone to put it in a good layout.
Professional, clean and appealing to the eye. Don't want it to look over crowded or busy.
Layout should feature 2-7 photos, without making the page look too busy. Can use any of the photos provided and you are welcome to crop them to change the orientation of the photo.
Content and typeface should fit in with logo and be modern but appeal to the female target audience of brides in Australia aged 22-40yo.
Advertisement is be be used in a bridal magazine and other print media for business advertising purposes.
Updates

Target Market(s)

Future brides in Australia aged 22 - 40yo - females only

Industry/Entity Type

Business

Colors
e34197
ffffff
eda3c7

Requirements
Must have
• White background
Should not have
• NO script writing as it doesn't fit with the logo.

```html
<!DOCTYPE html>
<html lang="en">
<head>
<meta charset="utf-8">
<title>Solenne Makeup Artistry – Advert</title>
<link href="https://fonts.googleapis.com/css2?family=Jost:wght@300;400&display=swap" rel="stylesheet">
<style>
  :root{
    --stage:#6e6b6b;
    --paper:#ffffff;
    --paper-shade:#ececec;
    --ink:#2f2f2f;
    --ink-soft:#555555;
    --muted:#8a8a8a;
    --footer:#3a3a3a;
    --footer-text:#e6e6e6;
    --accent:#e34197;
    --accent-soft:#eda3c7;
    --ring:#c9c9c9;
  }
  *{margin:0;padding:0;box-sizing:border-box}
  html,body{width:1200px;height:1000px;overflow:hidden}
  body{background:var(--stage);font-family:'Jost',sans-serif;color:var(--ink);position:relative}

  .advert{position:absolute;left:260px;top:20px;width:680px;height:960px;
    background:linear-gradient(180deg,var(--paper-shade) 0%,var(--paper) 18%,var(--paper) 82%,var(--paper-shade) 100%);
    overflow:hidden}

  .brand{position:absolute;top:54px;right:90px;text-align:right}
  .brand-name{font-weight:300;font-size:58px;letter-spacing:10px;color:var(--ink);line-height:1}
  .brand-tagline{font-weight:300;font-size:11px;letter-spacing:5px;color:var(--muted);margin-top:6px}

  .hero{position:absolute;left:0;top:150px;width:680px;height:400px;
    background:
      radial-gradient(ellipse 130px 150px at 360px 170px,#e3c2ad 0%,rgba(227,194,173,0) 100%),
      radial-gradient(ellipse 90px 110px at 200px 150px,#dcc0ae 0%,rgba(220,192,174,0) 100%),
      radial-gradient(ellipse 90px 110px at 540px 230px,#d9c4b8 0%,rgba(217,196,184,0) 100%),
      radial-gradient(ellipse 380px 260px at 340px 200px,#f7f7f7 0%,#e4e4e4 70%,var(--paper) 100%)}

  .intro{position:absolute;left:70px;top:570px;width:540px;text-align:center;
    font-size:11px;line-height:1.45;color:var(--ink-soft)}
  .intro p+p{margin-top:8px}

  .services{position:absolute;left:0;top:690px;width:680px;text-align:center;
    font-size:17px;letter-spacing:1px;color:var(--ink)}
  .services .sep{margin:0 8px;color:var(--muted)}

  .gallery{position:absolute;left:40px;top:728px;width:600px;display:flex;justify-content:space-between}
  .gallery-item{width:126px;height:126px;border-radius:50%;padding:8px;
    background:radial-gradient(circle,var(--ring) 60%,#f2f2f2 100%)}
  .gallery-photo{width:100%;height:100%;border-radius:50%}
  .photo-car{background:radial-gradient(circle at 40% 40%,#d8b49a,#b2463a 70%,#4d6a3a)}
  .photo-veil{background:radial-gradient(circle at 50% 45%,#c99c88,#6a5a5a 70%,#d9d9d9)}
  .photo-flowers{background:radial-gradient(circle at 50% 40%,#e7b9b2,#a06a4a 65%,#f4f0ee)}
  .photo-garden{background:radial-gradient(circle at 50% 50%,#ddb8a6,#3c6b3a 65%,#244a24)}

  .contact-bar{position:absolute;left:0;bottom:0;width:680px;height:64px;background:var(--footer);
    display:flex;align-items:center;justify-content:space-around;padding:0 20px;
    color:var(--footer-text);font-size:15px;font-weight:300;letter-spacing:.5px}
  .contact-bar svg{vertical-align:-3px;margin-right:6px}
</style>
</head>
<body>
  <main class="advert">
    <header class="brand">
      <div class="brand-name">SOLENNE</div>
      <div class="brand-tagline">MAKEUP ARTISTRY</div>
    </header>

    <div class="hero" role="img" aria-label="Soft white montage of a bride in a veil and strapless gown, shown in three angled portrait panels"></div>

    <section class="intro">
      <p>Following a lifelong interest and passion in the art of makeup and beauty products, Mara has launched Solenne Makeup Artistry. She has a wealth of knowledge and over 10 years experience with makeup and beauty.</p>
      <p>Offering a mobile makeup artistry and hairstyling service to Sydney metro, Castle Hill and surrounding areas, Mara is able to meet all your makeup and hairstyling needs, for bridal, formal, photographic, advertising, catwalk or any special event. She works with her clients to create their vision and exceed expectation.</p>
    </section>

    <h2 class="services">BRIDAL MAKEUP<span class="sep">|</span>HAIR STYLING SERVICES<span class="sep">|</span>SPECIAL OCCASION MAKEUP</h2>

    <section class="gallery">
      <div class="gallery-item"><div class="gallery-photo photo-car" role="img" aria-label="Bride seated in a red vintage car"></div></div>
      <div class="gallery-item"><div class="gallery-photo photo-veil" role="img" aria-label="Close portrait of a bride with dark hair and veil"></div></div>
      <div class="gallery-item"><div class="gallery-photo photo-flowers" role="img" aria-label="Bridal updo decorated with pink flowers"></div></div>
      <div class="gallery-item"><div class="gallery-photo photo-garden" role="img" aria-label="Bride with floral crown in a green garden"></div></div>
    </section>

    <footer class="contact-bar">
      <span class="contact-phone">
        <svg width="14" height="14" viewBox="0 0 24 24" aria-hidden="true"><path fill="currentColor" d="M6.6 10.8a15.1 15.1 0 0 0 6.6 6.6l2.2-2.2c.3-.3.7-.4 1-.2 1.1.4 2.3.6 3.6.6.6 0 1 .4 1 1V20c0 .6-.4 1-1 1A17 17 0 0 1 3 4c0-.6.4-1 1-1h3.5c.6 0 1 .4 1 1 0 1.3.2 2.5.6 3.6.1.3 0 .7-.2 1z"/></svg>Call Us: 0400 123 456
      </span>
      <span class="contact-web">www.solennemakeup.com.au</span>
      <span class="contact-email">mara@solennemakeup.com.au</span>
    </footer>
  </main>
</body>
</html>
```